Saffron Lantern food box

To design a label (sticker) for my Biriyani and Curries that comply with Australian food labeling regulations for cook chilled food.

one sticker that covers all 4 sides of the box

```html
<!DOCTYPE html>
<html lang="en">
<head>
<meta charset="utf-8">
<title>Saffron Lantern – Chicken &amp; Vegitable Cottage Pie label</title>
<link href="https://fonts.googleapis.com/css2?family=Oswald:wght@500&family=Roboto+Slab:wght@300&family=Roboto:wght@400;700;900&display=swap" rel="stylesheet">
<style>
  :root {
    --stage: #e8e8e8;
    --label-light: #ececea;
    --label-mid: #d9d9d6;
    --ink: #2d2d2d;
    --brand-band: #0d0d0d;
    --brand-text: #f29a2e;
    --title: #e8492a;
    --rule: #9a9a9a;
    --badge-red: #e8321f;
    --white: #ffffff;
    --green: #1fae4b;
    --photo-light: #f0dc98;
    --photo-mid: #c9a650;
    --photo-dark: #4f6d3a;
  }
  * { box-sizing: border-box; margin: 0; padding: 0; }
  html, body { width: 1200px; height: 1080px; overflow: hidden; }
  body { background: var(--stage); position: relative; font-family: "Roboto", sans-serif; color: var(--ink); }

  .label {
    position: absolute; left: 241px; top: 5px; width: 718px; height: 1070px;
    background: linear-gradient(160deg, var(--label-light) 0%, var(--label-mid) 55%, var(--label-light) 100%);
    overflow: hidden;
  }

  .brand-band {
    position: absolute; left: 0; top: 47px; width: 306px; height: 112px;
    background: var(--brand-band);
    display: flex; align-items: center; gap: 10px; padding-left: 22px;
  }
  .brand-dot { width: 16px; height: 16px; border-radius: 50%; background: var(--brand-text); }
  .brand-name { font-family: "Oswald", sans-serif; font-weight: 500; font-size: 30px; color: var(--brand-text); letter-spacing: 0.5px; }

  .product-title {
    position: absolute; left: 26px; top: 200px;
    font-family: "Oswald", sans-serif; font-weight: 500; font-size: 78px; line-height: 90px;
    color: var(--title); letter-spacing: -1px;
  }

  .title-rule { position: absolute; left: 0; top: 538px; width: 360px; height: 1px; background: var(--rule); }

  .description {
    position: absolute; left: 28px; top: 575px; width: 360px;
    font-family: "Roboto Slab", serif; font-weight: 300; font-size: 21px; line-height: 23px; color: var(--ink);
    white-space: nowrap;
  }

  .hero-photo {
    position: absolute; left: 343px; top: 50px; width: 740px; height: 780px; border-radius: 50%;
    border: 12px solid var(--white);
    background: radial-gradient(circle at 45% 30%, var(--photo-light) 0%, var(--photo-mid) 55%, var(--photo-dark) 100%);
    box-shadow: -6px 10px 24px rgba(0,0,0,0.25);
  }

  .promo-pill {
    position: absolute; left: 490px; top: 78px; width: 240px; height: 57px; z-index: 1;
    background: var(--white); border-radius: 28px 0 0 28px;
    display: flex; align-items: center; padding-left: 62px; gap: 6px;
  }
  .promo-pct { font-weight: 900; font-size: 30px; letter-spacing: -1px; }
  .promo-words { font-weight: 700; font-size: 17px; line-height: 17px; }
  .new-badge {
    position: absolute; left: 448px; top: 83px; width: 94px; height: 94px; border-radius: 50%; z-index: 2;
    background: var(--badge-red); border: 4px solid var(--white);
    color: var(--white); text-align: center; font-weight: 900;
    display: flex; flex-direction: column; justify-content: center; line-height: 18px;
  }
  .new-badge .big { font-size: 24px; }
  .new-badge .small { font-size: 16px; }

  .net-weight { position: absolute; left: 40px; top: 866px; font-size: 32px; display: flex; align-items: baseline; gap: 8px; }
  .net-weight .e-mark { font-size: 52px; line-height: 40px; }

  .info-row { position: absolute; left: 32px; top: 935px; height: 90px; display: flex; align-items: center; }
  .info-item { display: flex; align-items: center; justify-content: center; padding: 0 8px; border-right: 1px solid #b5b5b5; height: 80px; }
  .info-item:last-child { border-right: none; }
  .microwave { color: var(--green); flex-direction: column; align-items: flex-start; padding-left: 0; }
  .microwave .label-word { font-weight: 700; font-size: 14px; }
  .microwave .time { font-size: 48px; line-height: 44px; font-weight: 700; }
  .microwave .time small { font-size: 16px; font-weight: 400; }
  .ring { width: 68px; height: 68px; border-radius: 50%; border: 2px solid var(--ink); background: var(--white); display: flex; flex-direction: column; align-items: center; justify-content: center; text-align: center; }
  .serves .t1 { font-size: 15px; } .serves .t2 { font-size: 26px; font-weight: 700; line-height: 26px; }
  .energy .t1 { font-size: 13px; font-weight: 700; } .energy .t2 { font-size: 12px; font-weight: 700; }
  .energy .t3 { font-size: 10px; font-weight: 700; border: 1px solid var(--ink); border-radius: 6px; padding: 0 4px; margin-top: 2px; }
  .cert-round { width: 66px; height: 66px; border-radius: 50%; background: var(--ink); }
  .cert-tall { width: 50px; height: 98px; background: var(--ink); border: 2px solid var(--white); outline: 1px solid var(--ink); }

  .origin-box { position: absolute; left: 564px; top: 893px; width: 118px; height: 130px; }
  .origin-box .tag { background: var(--white); border-radius: 10px 10px 0 0; font-weight: 700; font-size: 10px; padding: 10px 8px 4px; }
  .origin-box .keep { background: var(--white); font-weight: 700; font-size: 10px; padding: 4px 8px 6px; }
  .origin-box .panel { height: 44px; background: var(--white); position: relative; }
  .origin-flag { position: absolute; right: 6px; top: -6px; width: 44px; height: 44px; border-radius: 50%; background: #1d3b8f; border: 2px solid var(--white); }
  .origin-box .made { font-weight: 700; font-size: 10px; padding-top: 6px; white-space: nowrap; }
</style>
</head>
<body>
  <main class="label">
    <div class="hero-photo" role="img" aria-label="Photo of a chicken and vegetable cottage pie in a white dish, golden mashed potato top"></div>

    <div class="brand-band">
      <span class="brand-dot"></span>
      <span class="brand-name">Saffron Lantern</span>
    </div>

    <h1 class="product-title">Chicken<br>&amp; Vegitable<br>Cottage Pie</h1>

    <div class="promo-pill">
      <span class="promo-pct">30%</span>
      <span class="promo-words">EXTRA<br>CHICKEN</span>
    </div>
    <div class="new-badge"><span class="big">NEW</span><span class="small">RECIPE</span></div>

    <div class="title-rule"></div>

    <p class="description">Tender, Australian chicken<br>in a thyme infused cream sauce<br>with a medley of onion, sweet<br>of white wine and topped with<br>pipings of creamy mashed patato.</p>

    <div class="net-weight"><span>350 g</span><span class="e-mark">℮</span></div>

    <div class="info-row">
      <div class="info-item microwave">
        <span class="label-word">Microwave</span>
        <span class="time">4<small>min</small></span>
      </div>
      <div class="info-item"><div class="ring serves"><span class="t1">serves</span><span class="t2">1</span></div></div>
      <div class="info-item"><div class="cert-round" role="img" aria-label="Health star rating badge"></div></div>
      <div class="info-item"><div class="ring energy"><span class="t1">Energy</span><span class="t2">497kj</span><span class="t3">PER 100g</span></div></div>
      <div class="info-item"><div class="cert-round" role="img" aria-label="Approved farming certification badge"></div></div>
      <div class="info-item"><div class="cert-tall" role="img" aria-label="Country of origin label"></div></div>
    </div>

    <div class="origin-box">
      <div class="tag">Serving Suggestion</div>
      <div class="keep">Keep refrigerated</div>
      <div class="panel"><div class="origin-flag" role="img" aria-label="Australian flag"></div></div>
      <div class="made">Produced in the Australia</div>
    </div>
  </main>
</body>
</html>
```